Menu Redesign - Upscale Restaurant

We are looking to have our lunch and dinner menus redesigned. We are looking to elevate the signs some, no emojis. We want a clean but elevated look, please refer to Marlow’s Dining Collective food menu and Vesper Tavola’s beverage menu. The company we’ve been using presented us with the attached menu / it’s filled with spelling and grammar errors.

Industry/Entity Type

Restaurant - Hospitality

```html
<!DOCTYPE html>
<html lang="en">
<head>
<meta charset="utf-8">
<title>Miss Odette’s Creole House – Lunch &amp; Drinks Menu</title>
<link rel="stylesheet" href="https://fonts.googleapis.com/css2?family=Playfair+Display:wght@500;600;700&family=Cormorant+Garamond:wght@500;600&family=Poppins:wght@400;500;600;700&display=swap">
<style>
:root{
  --backdrop:#8b8b8b;
  --paper:#ece6dc;
  --red:#c61f2e;
  --gold:#c49a55;
  --tan:#d8c19c;
  --ink:#1d1d1d;
  --muted:#3a3a3a;
}
*{box-sizing:border-box;margin:0;padding:0}
html,body{width:1200px;height:2734px;overflow:hidden}
body{background:var(--backdrop);font-family:"Poppins",sans-serif;color:var(--ink);position:relative}
.page{position:absolute;left:187px;width:825px;height:1167px;background:var(--paper);box-shadow:0 2px 10px rgba(0,0,0,.25)}
.page-lunch{top:165px}
.page-drinks{top:1403px}

/* masthead */
.brand{position:absolute;left:55px;top:52px;width:245px;display:flex;flex-direction:column;align-items:center;font-family:"Playfair Display",serif;font-weight:700;color:var(--red);line-height:1}
.brand-name{font-size:42px;letter-spacing:.5px}
.brand-sub{font-size:17px;letter-spacing:3px;text-transform:uppercase;margin-top:8px}
.masthead-rule{position:absolute;left:372px;top:53px;width:1px;height:99px;background:var(--red);opacity:.6}
.hours{position:absolute;left:446px;top:38px;width:360px}
.hours-title{font-family:"Playfair Display",serif;font-weight:600;font-size:22px;color:var(--red);text-transform:uppercase;letter-spacing:.5px;line-height:26px}
.hours-title.brunch{margin-top:6px}
.hours-line{font-family:"Cormorant Garamond",serif;font-weight:600;font-size:17px;text-transform:uppercase;line-height:19px}
.hours-note{font-family:"Cormorant Garamond",serif;font-weight:500;font-size:16px;line-height:21px}
.menu-rule{position:absolute;left:0;right:0;top:175px;height:5px;border-top:1px solid var(--red);border-bottom:1px solid var(--red)}
.menu-title{position:absolute;left:0;right:0;top:159px;text-align:center}
.menu-title span{background:var(--paper);padding:0 4px;font-family:"Playfair Display",serif;font-weight:600;font-size:30px;color:var(--red);letter-spacing:1px;line-height:34px}

/* sections */
.section-title{position:absolute;font-family:"Playfair Display",serif;font-weight:600;font-size:24px;color:var(--red);text-transform:uppercase;letter-spacing:.5px;line-height:29px}
.flourish{position:absolute;height:5px;border-radius:3px;background:var(--gold);opacity:.75}
.list{position:absolute;display:flex;flex-direction:column;justify-content:space-between}
.row{display:flex;align-items:flex-end;gap:2px}
.name{font-weight:500;font-size:11.5px;text-transform:uppercase;white-space:nowrap;line-height:14px}
.leader{flex:1;border-bottom:1px solid #555;margin-bottom:3px;min-width:8px}
.price{font-weight:500;font-size:11.5px;line-height:14px;white-space:nowrap}
.price sup{font-size:7px}
.plain-price{font-size:12px;font-weight:500}
.desc{font-size:6px;line-height:7.5px;color:var(--muted);margin-top:2px;max-width:175px}

/* page 1 */
.small-plates{left:45px;top:244px;width:191px;height:690px}
.sandwich-frame{position:absolute;left:287px;top:204px}
.sandwich-title{left:287px;top:222px;width:218px;text-align:center}
.sandwich-note{position:absolute;left:287px;width:218px;top:305px;text-align:center;font-size:10px}
.sandwiches{left:300px;top:332px;width:188px;height:396px}
.protein-box{position:absolute;left:285px;top:780px;width:211px;height:48px;background:var(--tan);border-radius:7px;padding:8px 10px;font-size:8px;line-height:10px;color:#4a4037}
.protein-box strong{display:block;font-size:9.5px;font-weight:600;color:var(--ink);margin-bottom:2px}
.dressing{position:absolute;left:285px;top:850px;width:222px;font-size:7.5px;line-height:10px}
.dressing strong{font-weight:600}
.entrees{left:551px;top:242px;width:200px;height:625px}
.notice{position:absolute;left:551px;top:892px;width:212px;height:32px;background:var(--tan);border-radius:7px;padding:4px 8px;font-size:6.5px;line-height:8px;text-align:center;color:#4a4037}
.sides-frame{position:absolute;left:45px;top:954px}
.sides-title{position:absolute;left:0;right:0;top:939px;text-align:center}
.sides-title span{background:var(--paper);padding:0 6px;font-family:"Playfair Display",serif;font-weight:600;font-size:24px;color:var(--red)}
.sides-col{position:absolute;top:976px;font-weight:700;font-size:9.5px;line-height:16.3px;text-transform:uppercase}
.sides-col sup{color:var(--red);font-size:7px}
.sides-divider{position:absolute;top:972px;width:1px;height:86px;background:var(--gold)}
.footer-note{position:absolute;left:0;right:0;text-align:center;font-size:9.5px;line-height:13px}
.footer-note.strong{font-weight:500;font-size:10px}

/* page 2 */
.beverages{left:45px;top:296px;width:187px;height:335px}
.spirits{left:45px;top:730px;width:187px;height:244px}
.cocktails{left:290px;top:322px;width:189px;height:660px}
.wine-frame{position:absolute;left:551px;top:228px}
.wine-title{left:551px;top:258px;width:223px;text-align:center;font-size:25px}
.wine{left:573px;top:318px;width:180px;height:190px}
.specials-frame{position:absolute;left:555px;top:594px}
.specials-title{left:573px;top:617px;width:190px}
.specials{left:573px;top:702px;width:180px;height:98px}
.specials .name{text-transform:none;font-size:12px}
.wine-grapes{display:flex;gap:16px}
.ornament-area{position:absolute;left:640px;top:875px;width:46px;height:102px;border-radius:23px 23px 20px 20px;background:var(--gold);opacity:.55}
.bottom-flourish{position:absolute;left:177px;top:1036px;width:472px;height:6px;border-radius:3px;background:var(--gold);opacity:.75}
</style>
</head>
<body>

<!-- ============ LUNCH PAGE ============ -->
<section class="page page-lunch">
  <div class="brand"><span class="brand-name">Miss Odette’s</span><span class="brand-sub">Creole House</span></div>
  <span class="masthead-rule"></span>
  <div class="hours">
    <h2 class="hours-title">Happy Hour Food &amp; Drinks</h2>
    <p class="hours-line">Monday to Friday 3:00PM-6:00PM</p>
    <p class="hours-note">Bar seats and high top tables by bar ONLY</p>
    <h2 class="hours-title brunch">Brunch</h2>
    <p class="hours-line">Saturday &amp; Sunday 10:00AM-4:00PM</p>
  </div>
  <div class="menu-rule"></div>
  <h1 class="menu-title"><span>LUNCH MENU</span></h1>

  <h2 class="section-title" style="left:45px;top:194px">Small Plates</h2>
  <div class="flourish" role="img" aria-label="Gold scroll ornament" style="left:45px;top:227px;width:190px"></div>
  <div class="list small-plates">
    <div class="item"><div class="row"><span class="name">Fried Devil Eggs</span><span class="leader"></span><span class="price"><sup>$</sup>13</span></div><p class="desc">Sweet relish, spiced whipped eggs with a choice of jumbo lump crab or shrimp for an upcharge.</p></div>
    <div class="item"><div class="row"><span class="name">Fried Green Tomatoes</span><span class="leader"></span><span class="price"><sup>$</sup>13</span></div><p class="desc">Sliced green tomatoes seasoned and battered in panko crumb. Add crab +$6.</p></div>
    <div class="item"><div class="row"><span class="name">Spinach Dip</span><span class="leader"></span><span class="price"><sup>$</sup>14</span></div><p class="desc">Fresh chopped spinach in a four cheese blend with tortilla chips. Add crab +$6.</p></div>
    <div class="item"><div class="row"><span class="name">Bayou Egg Rolls</span><span class="leader"></span><span class="price"><sup>$</sup>15</span></div><p class="desc">Diced chicken, peppers and cheese in an egg roll with remoulade dipping.</p></div>
    <div class="item"><div class="row"><span class="name">Hot Honey Salmon Bites</span><span class="leader"></span><span class="price"><sup>$</sup>15</span></div><p class="desc">Crispy salmon bites tossed in hot honey glaze with a side of house slaw.</p></div>
    <div class="item"><div class="row"><span class="name">Cup of Gumbo</span><span class="leader"></span><span class="price"><sup>$</sup>15</span></div><p class="desc">Andouille sausage, shrimp and chicken slow cooked in a cajun broth over rice.</p></div>
    <div class="item"><div class="row"><span class="name">Creole Wings</span><span class="leader"></span><span class="price"><sup>$</sup>16</span></div><p class="desc">Fried crispy bone-in wings tossed in your choice of our signature sauces.</p></div>
    <div class="item"><div class="row"><span class="name">Seafood Egg Rolls</span><span class="leader"></span><span class="price"><sup>$</sup>16</span></div><p class="desc">Chopped shrimp, crab meat and cheese rolled and fried with remoulade.</p></div>
    <div class="item"><div class="row"><span class="name">Voodoo Shrimp</span><span class="leader"></span><span class="price"><sup>$</sup>16</span></div><p class="desc">Fried shrimp tossed in voodoo sauce topped with jalapenos and blue cheese.</p></div>
    <div class="item"><div class="row"><span class="name">New Orleans Shrimp</span><span class="leader"></span><span class="price"><sup>$</sup>16</span></div><p class="desc">Creamy garlic cajun sauteed shrimp served with toasted bread.</p></div>
    <div class="item"><div class="row"><span class="name">Raw Oyster</span><span class="leader"></span><span class="price"><sup>$</sup>16</span></div><p class="desc">Fresh shucked blue point oysters over ice with lemon and mignonette.</p></div>
    <div class="item"><div class="row"><span class="name">Steak &amp; Cheese Rolls</span><span class="leader"></span><span class="price"><sup>$</sup>16</span></div><p class="desc">Philly steak, grilled onions, peppers, cheese and chipotle mayo.</p></div>
    <div class="item"><div class="row"><span class="name">Chargrilled Oysters</span><span class="leader"></span><span class="price"><sup>$</sup>17</span></div><p class="desc">Fresh shucked oysters grilled with cajun garlic butter and cheese blend.</p></div>
    <div class="item"><div class="row"><span class="name">Rockefeller Oysters</span><span class="leader"></span><span class="price"><sup>$</sup>18</span></div><p class="desc">Fresh shucked oysters stuffed with creamy spinach and cheese.</p></div>
    <div class="item"><div class="row"><span class="name">Seafood Basket</span><span class="leader"></span><span class="price"><sup>$</sup>18</span></div><p class="desc">Choice of battered catfish or fried golden shrimp with season fries.</p></div>
    <div class="item"><div class="row"><span class="name">Stuffed Shrimp</span><span class="leader"></span><span class="price"><sup>$</sup>18</span></div><p class="desc">Shrimp stuffed with crab meat, fried golden over jalapeno corn succotash.</p></div>
    <div class="item"><div class="row"><span class="name">Jambalaya Oysters</span><span class="leader"></span><span class="price"><sup>$</sup>22</span></div><p class="desc">Fresh shucked oysters stuffed with creamy cajun shrimp and crab.</p></div>
    <div class="item"><div class="row"><span class="name">Make it a Platter</span><span class="leader"></span><span class="price"><sup>$</sup>30</span></div><p class="desc">(Serves 3)<br>Mix 3 of your favorite starters.<br>(Each seafood starter added to platter is upcharged)</p></div>
  </div>

  <svg class="sandwich-frame" width="218" height="551" viewBox="0 0 218 551" aria-hidden="true"><path d="M14 1H204A13 13 0 0 0 217 14V537A13 13 0 0 0 204 550H14A13 13 0 0 0 1 537V14A13 13 0 0 0 14 1Z" fill="none" stroke="#c49a55" stroke-width="2"/></svg>
  <h2 class="section-title sandwich-title">Sandwiches<br>&amp; Salads</h2>
  <div class="flourish" role="img" aria-label="Gold scroll ornament" style="left:341px;top:290px;width:110px"></div>
  <p class="sandwich-note">Served with Seasoned Fries</p>
  <div class="list sandwiches">
    <div class="item"><div class="row"><span class="name">Ultimate Cheese Burger</span><span class="leader"></span><span class="price"><sup>$</sup>18</span></div><p class="desc">Beef patty topped with white cheddar, lettuce and tomato. Add bacon or egg.</p></div>
    <div class="item"><div class="row"><span class="name" style="font-size:10.5px">Miss Odette’s Chicken Sandwich</span><span class="leader"></span><span class="price"><sup>$</sup>18</span></div><p class="desc">Fried chicken breast with pickles, slaw and house sauce on brioche.</p></div>
    <div class="item"><div class="row"><span class="name">Catfish Sandwich</span><span class="leader"></span><span class="price"><sup>$</sup>18</span></div><p class="desc">Flash fried catfish filet, lettuce, tomato and remoulade sauce.</p></div>
    <div class="item"><div class="row"><span class="name">Salmon BLT</span><span class="leader"></span><span class="price"><sup>$</sup>19</span></div><p class="desc">Fresh salmon fried or grilled, bacon, chipotle mayo, lettuce and tomato on French bread.</p></div>
    <div class="item"><div class="row"><span class="name">Crab Cake Sandwich</span><span class="leader"></span><span class="price"><sup>$</sup>25</span></div><p class="desc">Fresh jumbo lump crab cake, deep-fried or pan-seared, topped with lettuce, tomato and remoulade.</p></div>
    <div class="item"><div class="row"><span class="name">Caesar Salad</span><span class="leader"></span><span class="price"><sup>$</sup>12</span></div><p class="desc">Romaine, parmesan, croutons and housemade caesar dressing.</p></div>
    <div class="item"><div class="row"><span class="name">Crispy Chicken House</span><span class="leader"></span><span class="price"><sup>$</sup>17</span></div><p class="desc">Field greens, dried cranberries, cherry tomatoes, boiled egg, cheddar, croutons and crispy chicken.</p></div>
    <div class="item"><div class="row"><span class="name">Grilled Pear &amp; Walnut</span><span class="leader"></span><span class="price"><sup>$</sup>19</span></div><p class="desc">Fresh greens, charred pear slices, red onion, cranberries, walnuts and blackened chicken.</p></div>
    <div class="item"><div class="row"><span class="name">Honey Caribbean Salmon</span><span class="leader"></span><span class="price"><sup>$</sup>22</span></div><p class="desc">Field greens, corn off the cob, tomatoes, cucumbers and buttermilk herb dressing.</p></div>
  </div>
  <div class="protein-box"><strong>Add Protein:</strong>Shrimp +7, Salmon +12, Blackened Chicken +10, Steak +16</div>
  <p class="dressing"><strong>Dressing Options:</strong> Honey Mustard, Balsamic Vinaigrette, Ranch, Caesar, Blue Cheese</p>

  <h2 class="section-title" style="left:551px;top:194px">Entrees</h2>
  <div class="list entrees">
    <div class="item"><div class="row"><span class="name">Cajun Salmon</span><span class="leader"></span><span class="price"><sup>$</sup>13</span></div><p class="desc">Perfectly seasoned pan-seared salmon topped with creamy creole sauce and 2 sides.</p></div>
    <div class="item"><div class="row"><span class="name">Miss Odette’s Fried Chicken</span><span class="leader"></span><span class="price"><sup>$</sup>23</span></div><p class="desc">1/2 chicken marinated in southern seasonings, fried golden with two sides.</p></div>
    <div class="item"><div class="row"><span class="name">Gumbo w/ Cornbread</span><span class="leader"></span><span class="price"><sup>$</sup>25</span></div><p class="desc">Rich roux with chicken, andouille, shrimp and scallion rice. Add crab leg +$10.</p></div>
    <div class="item"><div class="row"><span class="name">Fried Catfish</span><span class="leader"></span><span class="price"><sup>$</sup>25</span></div><p class="desc">Catfish fried golden or blackened served with two sides of your choice.</p></div>
    <div class="item"><div class="row"><span class="name">Pork Chops</span><span class="leader"></span><span class="price"><sup>$</sup>25</span></div><p class="desc">Fried or grilled pork chops smothered in southern gravy with two sides.</p></div>
    <div class="item"><div class="row"><span class="name">Bayou Pasta</span><span class="leader"></span><span class="price"><sup>$</sup>26</span></div><p class="desc">House-made cream sauce, peppers, tomatoes and onions over linguine with blackened chicken.</p></div>
    <div class="item"><div class="row"><span class="name">Jambalaya Pasta</span><span class="leader"></span><span class="price"><sup>$</sup>27</span></div><p class="desc">Shrimp, chicken, andouille and veggies in a cajun cream sauce. Rice option available.</p></div>
    <div class="item"><div class="row"><span class="name">Creole Herb Chicken</span><span class="leader"></span><span class="price"><sup>$</sup>28</span></div><p class="desc">Herb seasoned 1/2 chicken roasted tender, topped with creole sauce and 2 sides.</p></div>
    <div class="item"><div class="row"><span class="name">Catfish &amp; Grits</span><span class="leader"></span><span class="price"><sup>$</sup>28</span></div><p class="desc">Wild caught catfish blackened or fried over cheddar grits with cajun cream. Add crab +$10.</p></div>
    <div class="item"><div class="row"><span class="name">Shrimp &amp; Grits</span><span class="leader"></span><span class="price"><sup>$</sup>28</span></div><p class="desc">Sauteed shrimp, onions, peppers and tomatoes in cajun sauce over cheesy grits.</p></div>
    <div class="item"><div class="row"><span class="name">Oxtails</span><span class="leader"></span><span class="price"><sup>$</sup>40</span></div><p class="desc">Braised oxtails with butter beans served with your choice of two sides.</p></div>
    <div class="item"><div class="row"><span class="name">Caribbean Lamb Chops</span><span class="leader"></span><span class="price"><sup>$</sup>45</span></div><p class="desc">Lamb chops seasoned to perfection, sweet caribbean glaze and two sides.</p></div>
    <div class="item"><div class="row"><span class="name">Loaded Creole Pasta</span><span class="leader"></span><span class="price"><sup>$</sup>50</span></div><p class="desc">Sauteed shrimp, jumbo lump crab and crab leg over creamy cajun linguine.</p></div>
    <div class="item"><div class="row"><span class="name">2 Broiled Crab Cakes</span><span class="leader"></span><span class="price"><sup>$</sup>MKT</span></div><p class="desc">2 broiled jumbo lump crab cakes served with two sides.</p></div>
    <div class="item"><div class="row"><span class="name">Red Snapper</span><span class="leader"></span><span class="price"><sup>$</sup>MKT</span></div><p class="desc">Deep fried or roasted red snapper over jambalaya stew with two sides.</p></div>
  </div>
  <p class="notice">Please read menu descriptions carefully and be sure about what you are ordering. All checks will have 20% gratuity added. All parties 4+ will be on one check.</p>

  <svg class="sides-frame" width="735" height="116" viewBox="0 0 735 116" aria-hidden="true"><path d="M14 1H721A13 13 0 0 0 734 14V102A13 13 0 0 0 721 115H14A13 13 0 0 0 1 102V14A13 13 0 0 0 14 1Z" fill="none" stroke="#c49a55" stroke-width="1.5"/></svg>
  <h2 class="sides-title"><span>SIDES</span></h2>
  <div class="sides-col" style="left:107px">Cheesy Grits <sup>$</sup><sup>4</sup><br>Sautéed Spinach <sup>$5</sup><br>Seasoned Fries <sup>$5</sup><br>Fried Rice <sup>$6</sup><br>Garlic Mashed Potatoes <sup>$6</sup></div>
  <span class="sides-divider" style="left:305px"></span>
  <div class="sides-col" style="left:357px">Corn-Succotash <sup>$6</sup><br>Cornbread <sup>$6</sup><br>Spinach <sup>$7</sup><br>Sweet Potatoes <sup>$7</sup><br>Five Cheese Mac <sup>$8</sup></div>
  <span class="sides-divider" style="left:527px"></span>
  <div class="sides-col" style="left:579px;line-height:13px;top:978px">Collard Greens with<br>Smoked Turkey <sup>$8</sup><br>Broccolini <sup>$9</sup><br><span style="line-height:16.3px">Cajun Crab Fries <sup>$15</sup></span><br><span style="line-height:16.3px">Seafood Fried Rice <sup>$15</sup></span></div>

  <p class="footer-note strong" style="top:1080px">18% service charge on small parties of 4<br>20% service charge large parties of 6 or more.</p>
  <p class="footer-note" style="top:1109px;font-size:8.5px">Please alert your server if you have any food allergies. Consuming raw or undercooked meats, poultry, seafood, shellfish or eggs may increase your risk of foodborne illness.</p>
</section>

<!-- ============ DRINKS PAGE ============ -->
<section class="page page-drinks">
  <div class="brand"><span class="brand-name">Miss Odette’s</span><span class="brand-sub">Creole House</span></div>
  <span class="masthead-rule"></span>
  <div class="hours">
    <h2 class="hours-title">Happy Hour Food &amp; Drinks</h2>
    <p class="hours-line">Monday to Friday 3:00PM-6:00PM</p>
    <p class="hours-note">Bar seats and high top tables by bar ONLY</p>
    <h2 class="hours-title brunch">Brunch</h2>
    <p class="hours-line">Saturday &amp; Sunday 10:00AM-4:00PM</p>
  </div>
  <div class="menu-rule"></div>

  <h2 class="section-title" style="left:45px;top:222px">Beverages</h2>
  <div class="flourish" role="img" aria-label="Gold scroll ornament" style="left:45px;top:255px;width:150px"></div>
  <div class="list beverages">
    <div class="item"><div class="row"><span class="name">Soft Drinks</span><span class="leader"></span><span class="plain-price">4 (free refills)</span></div><p class="desc">Cola | Lemon-lime | Orange | Ginger ale | Pineapple | Cranberry juice</p></div>
    <div class="item"><div class="row"><span class="name">Ginger Beer</span><span class="leader"></span><span class="plain-price">4</span></div></div>
    <div class="item"><div class="row"><span class="name">Fresh Squeeze Lemonade</span><span class="leader"></span><span class="plain-price">5</span></div><p class="desc">Peach, Strawberry, Passion-fruit, Blackberry, Blueberry</p></div>
    <div class="item"><div class="row"><span class="name">Iced Tea</span><span class="leader"></span><span class="plain-price">5</span></div><p class="desc">Peach, Strawberry, Passion-fruit, Blackberry, Blueberry</p></div>
    <div class="item"><div class="row"><span class="name">Aqua Serena</span><span class="leader"></span><span class="plain-price">5</span></div></div>
    <div class="item"><div class="row"><span class="name">S. Valerio</span><span class="leader"></span><span class="plain-price">5</span></div></div>
    <div class="item"><div class="row"><span class="name">Blueberry Fizz</span><span class="leader"></span><span class="plain-price">12</span></div><p class="desc">Blueberry, Lime, Ginger beer</p></div>
    <div class="item"><div class="row"><span class="name">Pineapple Punch</span><span class="leader"></span><span class="plain-price">12</span></div><p class="desc">Pineapple juice, Orange juice, Peach syrup, Fresh lime juice</p></div>
  </div>

  <h2 class="section-title" style="left:45px;top:662px">Spirits</h2>
  <div class="flourish" role="img" aria-label="Gold scroll ornament" style="left:45px;top:695px;width:150px"></div>
  <div class="list spirits">
    <div class="item"><p class="name">Bourbon &amp; Whiskey</p><p class="desc">Ask your server for our full selection of small batch bourbons, ryes and blended whiskeys.</p></div>
    <div class="item"><p class="name">Scotch</p><p class="desc">Blended and single malt selections, 12 year.</p></div>
    <div class="item"><p class="name">Vodka</p><p class="desc">House vodka and premium French and Dutch labels.</p></div>
    <div class="item"><p class="name">Gin</p><p class="desc">London dry, botanical and floral selections.</p></div>
    <div class="item"><p class="name">Tequila</p><p class="desc">Blanco, reposado and añejo selections, plus a premium añejo pour.</p></div>
    <div class="item"><p class="name">Rum</p><p class="desc">Spiced, silver and dark rum selections.</p></div>
  </div>

  <h2 class="section-title" style="left:290px;top:222px;line-height:30px">Specialty<br>Cocktails</h2>
  <div class="flourish" role="img" aria-label="Gold scroll ornament" style="left:290px;top:288px;width:160px"></div>
  <div class="list cocktails">
    <div class="item"><div class="row"><span class="name">Pink Lady</span><span class="leader"></span><span class="price"><sup>$</sup>15</span></div><p class="desc">Tequila, orange liqueur, lime juice, strawberry-kiwi agave.</p></div>
    <div class="item"><div class="row"><span class="name">Blackberry French</span><span class="leader"></span><span class="price"><sup>$</sup>15</span></div><p class="desc">Floral gin, champagne, lemonade, white flowers.</p></div>
    <div class="item"><div class="row"><span class="name">Secrets</span><span class="leader"></span><span class="price"><sup>$</sup>15</span></div><p class="desc">Secret blend of 3 rums, tropical punch and fresh lime.</p></div>
    <div class="item"><div class="row"><span class="name">Peach Please</span><span class="leader"></span><span class="price"><sup>$</sup>16</span></div><p class="desc">House vodka, champagne, peach nectar, orange juice.</p></div>
    <div class="item"><div class="row"><span class="name" style="white-space:normal">Toasted Marshmallow<br>Espresso Martini</span><span class="leader"></span><span class="price"><sup>$</sup>16</span></div><p class="desc">House vodka, espresso liqueur, Irish cream, toasted marshmallows.</p></div>
    <div class="item"><div class="row"><span class="name">Miss Odette’s Hurricane</span><span class="leader"></span><span class="price"><sup>$</sup>16</span></div><p class="desc">Dark rum, light rum, passionfruit, lime juice, orange juice, grenadine.</p></div>
    <div class="item"><div class="row"><span class="name">Tsunami</span><span class="leader"></span><span class="price"><sup>$</sup>16</span></div><p class="desc">Blanco tequila, pineapple, orange, passionfruit, blue curacao topped with dark tequila.</p></div>
    <div class="item"><div class="row"><span class="name">Miskiri VIII</span><span class="leader"></span><span class="price"><sup>$</sup>17</span></div><p class="desc">Tequila, orange liqueur, blackberry, pineapple, cranberry, lemon juice.</p></div>
    <div class="item"><div class="row"><span class="name">Louisiana Tea</span><span class="leader"></span><span class="price"><sup>$</sup>17</span></div><p class="desc">Whiskey, honey mint syrup, fresh lemonade.</p></div>
    <div class="item"><div class="row"><span class="name">Odette’s Passion</span><span class="leader"></span><span class="price"><sup>$</sup>18</span></div><p class="desc">Cognac, orange liqueur, lemon juice, passionfruit.</p></div>
    <div class="item"><div class="row"><span class="name">Pineapple-Gria</span><span class="leader"></span><span class="price"><sup>$</sup>18</span></div><p class="desc">White sparkling wine, rum, pineapple punch.</p></div>
    <div class="item"><div class="row"><span class="name">Smoked in Fashion</span><span class="leader"></span><span class="price"><sup>$</sup>18</span></div><p class="desc">Whiskey, cubed sugar, black cherry, orange and cherry bitters.</p></div>
    <div class="item"><div class="row"><span class="name" style="font-size:10.5px">Smoked Tequila Old Fashion</span><span class="leader"></span><span class="price"><sup>$</sup>18</span></div><p class="desc">Aged tequila, orange liqueur, agave nectar, peach bitters, fresh orange peel.</p></div>
    <div class="item"><div class="row"><span class="name">Becky Sangria</span><span class="leader"></span><span class="price"><sup>$</sup>18</span></div><p class="desc">Red wine blend, cognac, tropical fruit punch and frozen popsicle.</p></div>
    <div class="item"><div class="row"><span class="name">Creole Island</span><span class="leader"></span><span class="price"><sup>$</sup>19</span></div><p class="desc">Cognac, orange liqueur, tropical punch.</p></div>
    <div class="item"><div class="row"><span class="name" style="font-size:10px">Margarita or Lemon Drop Flight</span><span class="leader"></span><span class="price"><sup>$</sup>20</span></div><p class="desc">Signature margarita and or lemon drops $20</p></div>
  </div>

  <svg class="wine-frame" width="223" height="323" viewBox="0 0 223 323" aria-hidden="true"><path d="M14 1H209A13 13 0 0 0 222 14V309A13 13 0 0 0 209 322H14A13 13 0 0 0 1 309V14A13 13 0 0 0 14 1Z" fill="none" stroke="#c49a55" stroke-width="2"/></svg>
  <h2 class="section-title wine-title">Wine &amp; Bubbly</h2>
  <div class="flourish" role="img" aria-label="Gold scroll ornament" style="left:590px;top:294px;width:150px"></div>
  <div class="list wine">
    <div class="item"><div class="row"><span class="name">Reds</span><span class="leader"></span><span class="price"><sup>$</sup>6</span></div><p class="desc wine-grapes"><span>Cabernet<br>Merlot</span><span>Pinot Noir<br>Sweet Red Blend</span></p></div>
    <div class="item"><div class="row"><span class="name">White</span><span class="leader"></span><span class="price"><sup>$</sup>6</span></div><p class="desc">Moscato, Pinot Grigio, Sauvignon Blanc, Chardonnay</p></div>
    <div class="item"><div class="row"><span class="name">Mesa Ridge Chardonnay</span><span class="leader"></span><span class="price"><sup>$</sup>7</span></div></div>
    <div class="item"><div class="row"><span class="name">Mesa Ridge Cabernet</span><span class="leader"></span><span class="price"><sup>$</sup>7</span></div></div>
    <div class="item"><div class="row"><span class="name">Sandpiper Moscato</span><span class="leader"></span><span class="price"><sup>$</sup>7</span></div></div>
    <div class="item"><div class="row"><span class="name">Fennwood Chardonnay</span><span class="leader"></span><span class="price"><sup>$</sup>10</span></div></div>
    <div class="item"><div class="row"><span class="name">Fennwood Cabernet</span><span class="leader"></span><span class="price"><sup>$</sup>10</span></div></div>
  </div>

  <svg class="specials-frame" width="219" height="245" viewBox="0 0 219 245" aria-hidden="true"><path d="M14 1H205A13 13 0 0 0 218 14V231A13 13 0 0 0 205 244H14A13 13 0 0 0 1 231V14A13 13 0 0 0 14 1Z" fill="none" stroke="#c49a55" stroke-width="2"/></svg>
  <h2 class="section-title specials-title" style="line-height:25px">Lunch Drink<br>Specials</h2>
  <div class="flourish" role="img" aria-label="Gold scroll ornament" style="left:573px;top:674px;width:170px"></div>
  <div class="list specials">
    <div class="item"><div class="row"><span class="name">Miss Odette’s Hurricane</span><span class="leader"></span><span class="price"><sup>$</sup>7</span></div><p class="desc">Peach, Strawberry, Passion-fruit, Blackberry, Blueberry</p></div>
    <div class="item"><div class="row"><span class="name">Signature Margarita</span><span class="leader"></span><span class="plain-price">7</span></div><p class="desc">Tequila, Orange liqueur, Sour mix add a flavor.</p></div>
    <div class="item"><div class="row"><span class="name">Signature Margarita</span><span class="leader"></span><span class="plain-price">7</span></div><p class="desc">Tequila, Orange liqueur, Sour mix add a flavor.</p></div>
  </div>

  <div class="ornament-area" role="img" aria-label="Gold scroll ornament with droplet"></div>
  <div class="bottom-flourish" role="img" aria-label="Gold scroll divider ornament"></div>
  <p class="footer-note" style="top:1081px">Please alert your server if you have any food allergies.<br>Consuming raw or undercooked meats, poultry, seafood, shellfish or eggs may increase your risk of foodborne illness</p>
</section>

</body>
</html>
```